Bright Meadow Counseling Business Card design with a visually interesting use of Space

I need business cards that are luxurious and give a peaceful, calm vibe. I also had some letterhead designed, and i like the look of it also, it's attached with the logo design for reference/ ideas but feel free to be creative.

Target Market(s)

High end luxurious client who needs counseling

Industry/Entity Type

Marriage and Family Therapy

Contact Information for Business Card

Mira Kowalczyk MS LMFT/ or Toby Hallett address 4150 Larkin Suite 600

Font styles to use
Sans Serif

Colors
0054AA
0677BA
7BADD7
CADEEF
E8F1F8
0094D4
00A9DD
6FCCEA
C7EBF8
E9F6FB
A7469A
B969AE
D3A5CF
EDDBEB
F8F0F9
6B429C
8869AF
B7A5CE
E3DAEB
F3F0F8

Requirements
Must have
• Logo and color scheme but be simple modern and luxurious
Nice to have
• I'd like to incorporate some elelmets from the logo and letterhead into a simple modern card

```html
<!DOCTYPE html>
<html lang="en">
<head>
<meta charset="UTF-8">
<title>Bright Meadow Counseling – Business Card</title>
<link rel="stylesheet" href="https://fonts.googleapis.com/css2?family=Montserrat:wght@300;400;700&display=swap">
<style>
  :root{
    --backdrop:#a07ab6;
    --card:#f6f6f7;
    --ink:#1c1c1e;
    --text:#55575a;
    --teal:#1f7f88;
    --aqua:#3bb3bd;
    --magenta:#a3246c;
    --plum:#a7469a;
    --violet:#6b429c;
    --sky:#6fccea;
  }
  *{box-sizing:border-box;margin:0;padding:0}
  html,body{width:1200px;height:1200px;overflow:hidden}
  body{
    background:var(--backdrop);
    font-family:"Montserrat",sans-serif;
    display:flex;flex-direction:column;align-items:center;justify-content:center;gap:56px;
  }
  .card{
    position:relative;width:900px;height:510px;border-radius:26px;
    background:linear-gradient(135deg,#ffffff 0%,var(--card) 100%);
    box-shadow:0 18px 40px rgba(60,30,80,.25);
    overflow:hidden;
  }
  .brand-name{
    font-weight:300;color:var(--ink);letter-spacing:.5px;white-space:nowrap;
  }
  .brand-dot{position:absolute;border-radius:50%;background:var(--plum);opacity:.85}

  /* front */
  .front .brand-name{position:absolute;right:82px;top:140px;font-size:40px}
  .front .brand-dot{width:58px;height:58px;right:60px;top:60px}
  .person{position:absolute;left:78px;top:232px}
  .person-name{font-weight:700;font-size:34px;color:var(--teal);letter-spacing:.3px}
  .person-title{font-weight:400;font-size:22px;color:var(--magenta);margin-top:2px}
  .divider{position:absolute;left:78px;top:331px;width:740px;height:4px;display:flex;gap:5px}
  .divider span{flex:1}
  .divider .d1{background:var(--violet)}
  .divider .d2{background:var(--magenta)}
  .divider .d3{background:var(--magenta)}
  .divider .d4{background:var(--aqua)}
  .contact{position:absolute;left:78px;top:364px;list-style:none}
  .contact li{display:flex;align-items:center;gap:16px;font-size:23px;color:var(--text);height:30px;letter-spacing:.4px}
  .contact svg{width:23px;height:23px;flex:none}
  .location{position:absolute;right:82px;top:364px;text-align:right;font-size:23px;color:var(--text);letter-spacing:.4px}
  .location p{height:30px;line-height:30px}
  .web{font-weight:700;color:var(--teal)}

  /* back */
  .back .brand-name{position:absolute;left:0;right:0;top:228px;text-align:center;font-size:52px}
  .back .brand-dot{width:96px;height:96px;left:680px;top:110px}
  .back .web{position:absolute;left:0;right:0;bottom:52px;text-align:center;font-size:24px;letter-spacing:.3px}
</style>
</head>
<body>

<section class="card front">
  <span class="brand-dot"></span>
  <p class="brand-name">Bright Meadow Counseling</p>

  <div class="person">
    <h1 class="person-name">Mira Kowalczyk</h1>
    <p class="person-title">MS LMFT</p>
  </div>

  <div class="divider"><span class="d1"></span><span class="d2"></span><span class="d3"></span><span class="d4"></span></div>

  <ul class="contact">
    <li>
      <svg viewBox="0 0 24 24" aria-hidden="true"><circle cx="12" cy="12" r="12" fill="var(--magenta)"/><path d="M8.2 6.5l2 2.3-1.1 1.5c.8 1.7 2 2.9 3.6 3.7l1.5-1.1 2.3 2-1.1 2c-4.3-.2-8.2-4.1-8.4-8.4z" fill="#fff"/></svg>
      555-214-0187
    </li>
    <li>
      <svg viewBox="0 0 24 24" aria-hidden="true"><circle cx="12" cy="12" r="12" fill="var(--magenta)"/><rect x="8.5" y="5.8" width="7" height="4" fill="#fff"/><rect x="6.3" y="10.3" width="11.4" height="5" rx="1" fill="#fff"/><rect x="8.5" y="14.3" width="7" height="3.6" fill="#fff" stroke="var(--magenta)" stroke-width=".8"/></svg>
      555-214-0192
    </li>
    <li>
      <svg viewBox="0 0 24 24" aria-hidden="true"><circle cx="12" cy="12" r="12" fill="var(--magenta)"/><rect x="6.3" y="8" width="11.4" height="8" fill="#fff"/><path d="M6.6 8.3l5.4 4.3 5.4-4.3" fill="none" stroke="var(--magenta)" stroke-width="1"/></svg>
      hello@brightmeadow.com
    </li>
  </ul>

  <div class="location">
    <p>2291 Willow Court</p>
    <p>Juneau, Alaska 99801</p>
    <p class="web">www.brightmeadow.com</p>
  </div>
</section>

<section class="card back">
  <span class="brand-dot"></span>
  <p class="brand-name">Bright Meadow Counseling</p>
  <p class="web">www.brightmeadow.com</p>
</section>

</body>
</html>
```